Werbetafel für Immobilienverwaltung
Zielgruppe
Wir sind im Kern eine Immobilienverwaltung, daher richten wir uns an Eigentümer/Investoren/Kapitalanleger. Neben der Verwaltung welche auch durch Hausmeisterservice (Grünarbeiten usw.) erweitert werden kann, bieten wir die Gutachtenerstellung sowie den Vertrieb (Maklertätigkeit in Verkauf sowie Vermietung) an.
Ein großer Vorteil ist unsere Digitale Arbeitsweise (noch keine Selbstverständlichkeit in der Branche).
Aufgabenstellung
Ziel ist es, das Unternehmen unaufdringlich jedoch wirksam und informativ auf einer Werbetafel zu präsentieren.
Maße der Tafel, welche sich im ausgangsbereich eines großen Lebensmittelunternehmens befindet, ist B 320cm x H 120cm.
Die Kundschaft läuft in ca. 1m Entfernung an der Tafel vorbei, sie sollte also von nahem nicht zu überrumpelt wirken.
Unser Logo sowie Telefonnummer sollte iwie untergebracht werden.
Gern auch eigene Ideen umsetzen falls Ihr welche habt.

```html
<!DOCTYPE html>
<html lang="de">
<head>
<meta charset="utf-8">
<title>Veltra Immobilien – Werbetafel</title>
<link rel="stylesheet" href="https://fonts.googleapis.com/css2?family=Montserrat:wght@500;600;700;800&display=swap">
<style>
  :root {
    --page-bg: #f2f3f7;
    --board-bg: #ffffff;
    --brand-red: #7a1716;
    --stone: #8a8a86;
    --ink-grey: #555555;
  }
  * { margin: 0; padding: 0; box-sizing: border-box; }
  html, body {
    width: 1200px; height: 1200px; overflow: hidden;
    background: var(--page-bg);
    font-family: "Montserrat", Arial, sans-serif;
  }
  .billboard {
    position: absolute; left: 50px; top: 383px;
    width: 1100px; height: 434px;
    background: var(--board-bg);
    overflow: hidden;
  }
  .band { position: absolute; left: 0; width: 100%; height: 28px; background: var(--brand-red); }
  .band--top { top: 0; }
  .band--bottom { bottom: 0; }

  .brand-mark {
    position: absolute; left: 42px; top: 196px;
    display: flex; align-items: center; gap: 10px;
    font-weight: 700; font-size: 30px; color: var(--stone);
    letter-spacing: 0.5px;
  }
  .brand-mark__square { width: 16px; height: 16px; background: var(--stone); }

  .gallery { position: absolute; left: 0; top: 28px; width: 560px; height: 378px; }

  .headline { position: absolute; left: 555px; top: 60px; color: var(--brand-red); white-space: nowrap; }
  .headline__lead { font-size: 33px; line-height: 1.1; font-weight: 700; }
  .headline__main { font-size: 46px; line-height: 1.25; margin-top: 6px; font-weight: 800; }

  .company { position: absolute; left: 557px; top: 246px; width: 386px; }
  .company__name {
    font-weight: 600; font-size: 40px; color: var(--brand-red);
    padding-bottom: 6px; border-bottom: 1px solid var(--stone);
    white-space: nowrap;
  }
  .company__tagline {
    margin-top: 8px; padding-left: 84px;
    font-size: 12.5px; font-weight: 500; color: var(--ink-grey); letter-spacing: 0.4px;
    white-space: nowrap;
  }

  .contact {
    position: absolute; left: 557px; top: 374px;
    display: flex; align-items: center; gap: 20px;
    font-size: 19px; color: var(--ink-grey);
  }
  .contact__item { display: flex; align-items: center; gap: 11px; }
  .contact__icon { width: 22px; height: 22px; background: var(--brand-red); display: flex; align-items: center; justify-content: center; }
  .contact__phone { font-weight: 600; }
  .contact__web { font-weight: 500; font-size: 17px; }
</style>
</head>
<body>
  <main class="billboard">
    <div class="band band--top"></div>

    <div class="brand-mark"><span class="brand-mark__square"></span>Veltra</div>

    <svg class="gallery" viewBox="0 0 560 378" width="560" height="378">
      <defs>
        <linearGradient id="fill-cathedral" x1="0" y1="0" x2="1" y2="1">
          <stop offset="0" stop-color="#e4e4e4"/>
          <stop offset="1" stop-color="#6e6e6e"/>
        </linearGradient>
        <linearGradient id="fill-river" x1="0" y1="0" x2="0" y2="1">
          <stop offset="0" stop-color="#5e5e5e"/>
          <stop offset="1" stop-color="#dcdcdc"/>
        </linearGradient>
        <linearGradient id="fill-bridge" x1="0" y1="0" x2="0" y2="1">
          <stop offset="0" stop-color="#b97a78"/>
          <stop offset="1" stop-color="#8e3533"/>
        </linearGradient>
      </defs>
      <polygon role="img" aria-label="Foto: Dom mit zwei Türmen in Schwarzweiß"
               points="267,-25 384,92 267,209 150,92" fill="url(#fill-cathedral)"/>
      <polygon role="img" aria-label="Foto: Stahlbrücke über dem Fluss mit Altstadt, rot getönt"
               points="393,97 510,214 393,331 276,214" fill="url(#fill-bridge)"/>
      <polygon role="img" aria-label="Foto: Spiegelung der Stadt im Fluss in Schwarzweiß"
               points="267,219 384,336 267,453 150,336" fill="url(#fill-river)"/>
    </svg>

    <div class="headline">
      <p class="headline__lead">Sie suchen, wir finden</p>
      <p class="headline__main">Ihre Traumimmobilie</p>
    </div>

    <div class="company">
      <p class="company__name">Veltra Immobilien</p>
      <p class="company__tagline">WIR KÜMMERN UNS UM IHR ZUHAUSE</p>
    </div>

    <div class="contact">
      <div class="contact__item">
        <span class="contact__icon">
          <svg width="14" height="14" viewBox="0 0 24 24" aria-hidden="true">
            <path fill="#fff" d="M6.6 10.8a15.1 15.1 0 0 0 6.6 6.6l2.2-2.2a1 1 0 0 1 1-.25 11.4 11.4 0 0 0 3.6.57 1 1 0 0 1 1 1V20a1 1 0 0 1-1 1A17 17 0 0 1 3 4a1 1 0 0 1 1-1h3.5a1 1 0 0 1 1 1c0 1.25.2 2.45.57 3.57a1 1 0 0 1-.25 1z"/>
          </svg>
        </span>
        <span class="contact__phone">0400 - 318 27 64</span>
      </div>
      <div class="contact__item">
        <span class="contact__icon">
          <svg width="14" height="14" viewBox="0 0 24 24" aria-hidden="true" fill="none" stroke="#fff" stroke-width="1.8">
            <circle cx="12" cy="12" r="9"/>
            <ellipse cx="12" cy="12" rx="4" ry="9"/>
            <line x1="3" y1="12" x2="21" y2="12"/>
            <line x1="4.5" y1="7.5" x2="19.5" y2="7.5"/>
            <line x1="4.5" y1="16.5" x2="19.5" y2="16.5"/>
          </svg>
        </span>
        <span class="contact__web">www.veltra-haus.de</span>
      </div>
    </div>

    <div class="band band--bottom"></div>
  </main>
</body>
</html>
```